Outpatient Mental Health Clinic needs a good brochure

We are an outpatient clinic in Michigan, USA and provide therapy and evaluation services for adults, adolescents, and children. Our psychologists, social workers, and counselors help individuals who present with a host of psychological difficulties. Our goal for the brochure is to give an overview of our services so that our marketing person can pass them out to physicians and other referral sources.

Target Market(s)

Our target market are patients who are seeking referrals through their primary care physicians.

Industry/Entity Type

Clinic

Font styles to use
Serif
Sans Serif

Colors
fbf289
f68d4c
f37122
ffffff

Requirements
Must have
• My project must be illustrative enough to show what services are provided. Pictures of individuals is also important.
Nice to have
• In addition to content I would like to have pictures of individuals.

```html
<!DOCTYPE html>
<html lang="en">
<head>
<meta charset="utf-8">
<title>Clinic Brochure – Front and Inside</title>
<link rel="stylesheet" href="https://fonts.googleapis.com/css2?family=Oswald:wght@500&family=Hind:wght@400&family=Nunito:wght@800&family=Great+Vibes&family=Arimo:wght@400&display=swap">
<style>
  :root {
    --slate: #4a4657;
    --slate-deep: #3f3b4b;
    --coral: #f0707a;
    --heading: #ee5d69;
    --ink: #4b4b4b;
    --paper: #ffffff;
    --canvas: #ffffff;
    --beige: #f3e3cc;
    --scrub: #6f79c9;
  }
  * { box-sizing: border-box; margin: 0; padding: 0; }
  html, body { width: 1200px; height: 1200px; overflow: hidden; background: var(--canvas); }
  body { position: relative; font-family: "Hind", sans-serif; color: var(--ink); }

  .side-label {
    position: absolute; font-family: "Arimo", sans-serif; font-size: 36px; color: #111;
  }
  .side-label.front { left: 72px; top: 272px; }
  .side-label.inside { left: 64px; top: 820px; }

  .sheet {
    position: absolute; left: 218px; width: 755px; height: 536px;
    background: var(--paper); box-shadow: 0 2px 6px rgba(0,0,0,.45); overflow: hidden;
  }
  .sheet.front { top: 38px; }
  .sheet.inside { top: 628px; }

  .panel { position: absolute; top: 0; height: 100%; width: 252px; }
  .panel.p1 { left: 0; } .panel.p2 { left: 251px; } .panel.p3 { left: 503px; }

  .copy { position: absolute; left: 20px; width: 214px; }
  .heading {
    font-family: "Oswald", sans-serif; font-weight: 500; font-size: 16px;
    color: var(--heading); letter-spacing: .2px; margin-bottom: 10px; line-height: 1;
  }
  .body-text { font-size: 8.2px; line-height: 10.8px; margin-bottom: 11px; }

  .photo { position: absolute; }
  .photo.nurse {
    left: 0; top: 298px; width: 252px; height: 238px;
    background: linear-gradient(to bottom, rgba(255,255,255,1) 0%, rgba(236,214,190,.6) 25%, #d9c2a6 55%, #a9bfe0 80%, #8fa9d6 100%);
  }
  .photo.consult {
    left: 0; top: 100px; width: 252px; height: 340px;
    background: linear-gradient(160deg, #f6ead8 0%, var(--beige) 45%, #e7b8b0 75%, #c98a8f 100%);
  }
  .photo.team {
    left: 0; top: 200px; width: 503px; height: 336px;
    background: linear-gradient(to bottom, rgba(255,255,255,1) 0%, #d8d2c4 22%, #8c8fb4 55%, var(--scrub) 75%, #4b4f9c 100%);
  }

  .cover-shapes { position: absolute; left: 0; top: 0; width: 252px; height: 536px; }
  .clinic-name {
    position: absolute; left: 21px; top: 28px;
    font-family: "Nunito", sans-serif; font-weight: 800; font-size: 36px; line-height: 30px; color: #fff;
  }
  .tagline {
    position: absolute; right: 20px; top: 424px; text-align: right;
    font-family: "Great Vibes", cursive; font-size: 17px; line-height: 16px; color: #fff;
  }
  .brand {
    position: absolute; left: 21px; top: 494px;
    font-family: "Nunito", sans-serif; font-weight: 800; font-size: 19px; color: #fff;
  }

  .contact {
    position: absolute; left: 21px; top: 432px; width: 210px; height: 83px;
    border: 1px solid var(--coral); border-radius: 8px;
  }
  .contact-title {
    position: absolute; left: 68px; top: -8px; width: 74px; height: 14px;
    background: var(--slate); color: #fff; font-family: "Hind", sans-serif; font-weight: 400;
    font-size: 9.5px; line-height: 15px; text-align: center; letter-spacing: .2px;
  }
  .contact-list { position: absolute; left: 12px; top: 13px; list-style: none; font-size: 8px; line-height: 12.6px; }
  .contact-list li { display: flex; align-items: center; gap: 4px; }
  .contact-list li.plain { padding-left: 12px; }
  .contact-list svg { width: 8px; height: 8px; flex: none; }

  .wave-band { position: absolute; left: 0; top: 0; width: 755px; height: 110px; }
</style>
</head>
<body>

<div class="side-label front">Front</div>
<div class="side-label inside">Inside</div>

<!-- Outside of the tri-fold -->
<section class="sheet front">
  <div class="panel p1">
    <div class="copy" style="top:22px">
      <h2 class="heading">HEADING</h2>
      <p class="body-text">vitaes ditas nusam eum sitas andestibus magnimped-it a comnis alit ilitatiat andit evellabore et fuga. Ovid maximil laborumque dolut auta nullore henimusdam eost, ulligna tibusa quodit, ni dellent veliquo tem ea vit hictatenti blacess imuscii strumque maio</p>
      <p class="body-text">Ihiliassunt quia quia volestotatem fuga. Berovit ate-moll atusam fugit am voluptas assinctiis modi seque venitatur? Ribus, cullab ium que volut labora dellessit, sequi doluptaquis et dis dolupta se sit, sin ratetur sit od qui di intur rerrore icabo. Nam, consequ iasit, asperume pa dem rehendi gnatet, cum dolo everrum endiciis mi, quia custi cor sit de ma consera tatemo-lupta aut de quia eost fuga. Icime et optio beatet fugit autectur, coraecto dolest voluptat.</p>
      <h2 class="heading" style="margin-top:4px">HEADING</h2>
      <p class="body-text">Dolestionet faccus repreptur mintio to dollent, quiam, sim quas voloreris ea quas serspis asit, sequi con-sendis isci torpor sequia ipid molo est aut minum</p>
    </div>
    <div class="photo nurse" role="img" aria-label="Photo of a nurse gently treating a patient's arm"></div>
  </div>

  <div class="panel p2">
    <div class="copy" style="top:20px">
      <p class="body-text">impor re am quis essin nis dereped mosam hilit aut quo blabori tiorem. Debit veribus et ut quo vidusdam fugit facepudi alit, con cuptatempor molo ea dollicip-sus solorio omnis ut asint mo optas simenimpor ma dolore vel inctorrum qui repersp editati oremque eosto torrumq uisque volorpo rrovidus nem quae parum ne et auditaturest quiam ad que odio. Et et, expland aecti-aesti comnienducid quiam la cus alique solupissit ea as ipsum re porpore ssequi derumet, sam, si voluptis exeruptaque doleser rumqui unt.</p>
      <h2 class="heading" style="margin-top:14px">HEADING</h2>
      <p class="body-text">vitaes ditas nusam eum sitas andestibus magnimped-it a comnis alit ilitatiat andit evellabore et fuga. Ovid maximil laborumque dolut auta nullore henimusdam eost, ulligna tibusa quodit, ni dellent veliquo tem ea vit hictatenti blacess imuscii strumque maio</p>
      <p class="body-text">Ihiliassunt quia quia volestotatem fuga. Berovit ate-moll atusam fugit am voluptas assinctiis modi seque venitatur? Ribus, cullab ium que volut labora dellessit, sequi doluptaquis et dis dolupta se sit, sin ratetur sit od qui di intur rerrore icabo. Nam, consequ iasit, asperume pa dem rehendi gnatet, cum dolo everrum endiciis mi, quia custi cor sit de ma consera tatemo-lupta aut de quia eost fuga. Icime et optio beatet fugit autectur, coraecto dolest voluptat.</p>
    </div>

    <div class="contact">
      <div class="contact-title">Contact Us</div>
      <ul class="contact-list">
        <li class="plain">Address</li>
        <li><svg viewBox="0 0 10 10"><path d="M5 0.5a3.2 3.2 0 0 0-3.2 3.2C1.8 6 5 9.5 5 9.5S8.2 6 8.2 3.7A3.2 3.2 0 0 0 5 .5zm0 4.5a1.3 1.3 0 1 1 0-2.6 1.3 1.3 0 0 1 0 2.6z" fill="#f0707a"/></svg>Michigan, USA</li>
        <li><svg viewBox="0 0 10 10"><circle cx="5" cy="5" r="4.3" fill="none" stroke="#f0707a" stroke-width="1"/><path d="M3.4 3c.3-.3.6-.3.8 0l.4.6c.1.2 0 .4-.2.6.3.6.7 1 1.3 1.3.2-.2.4-.3.6-.2l.6.4c.3.2.3.5 0 .8-.4.4-1 .4-1.6.1C4.6 6.2 3.8 5.4 3.4 4.6c-.3-.6-.3-1.2 0-1.6z" fill="#f0707a"/></svg>+123456789</li>
        <li><svg viewBox="0 0 10 10"><rect x="1" y="2.3" width="8" height="5.6" fill="#f0707a"/><path d="M1 2.6l4 3 4-3" fill="none" stroke="#fff" stroke-width=".8"/></svg>emailid@email.com</li>
        <li><svg viewBox="0 0 10 10"><circle cx="5" cy="5" r="4" fill="#f0707a"/><path d="M1 5h8M5 1c-1.6 2.2-1.6 5.8 0 8M5 1c1.6 2.2 1.6 5.8 0 8" fill="none" stroke="#fff" stroke-width=".6"/></svg>www.websitename.com</li>
      </ul>
    </div>
  </div>

  <div class="panel p3">
    <div class="photo consult" role="img" aria-label="Photo of a doctor showing an information booklet to a young female patient"></div>
    <svg class="cover-shapes" viewBox="0 0 252 536" aria-hidden="true">
      <path d="M0 0H252V72C190 108 100 124 0 112Z" fill="var(--slate)"/>
      <path d="M0 112C100 124 190 108 252 72V96C190 130 100 146 0 126Z" fill="var(--coral)"/>
      <path d="M0 450C60 400 150 370 252 390V536H0Z" fill="var(--coral)"/>
      <path d="M0 456C70 414 150 396 252 410V536H0Z" fill="var(--slate)"/>
    </svg>
    <h1 class="clinic-name">clinic<br>name</h1>
    <p class="tagline">For patients who are<br>seeking referrals through<br>their primary care physicians</p>
    <div class="brand">logo</div>
  </div>
</section>

<!-- Inside of the tri-fold -->
<section class="sheet inside">
  <svg class="wave-band" viewBox="0 0 755 110" aria-hidden="true">
    <defs>
      <linearGradient id="band-fill" x1="0" y1="0" x2="1" y2="0">
        <stop offset="0" stop-color="#e9727c"/>
        <stop offset=".55" stop-color="#8a5a6c"/>
        <stop offset="1" stop-color="var(--slate)"/>
      </linearGradient>
    </defs>
    <path d="M0 0H755V44C640 86 540 96 430 78C300 56 160 26 0 24Z" fill="url(#band-fill)"/>
    <path d="M755 44C640 86 540 96 430 78C560 92 660 82 755 52Z" fill="var(--slate-deep)"/>
  </svg>

  <div class="panel p1">
    <div class="copy" style="top:52px">
      <h2 class="heading">HEADING</h2>
      <p class="body-text">Min num etur? Quis eos moluptatem estiust, sun-torenihil idita consequunte name nonest, asimusaes aligeniendis nimporem quis sit aborit landiciasped que repti verchil iquaepe lessum eum ius mos idebis minto doluptas exerovita int facitec turibus.</p>
      <p class="body-text">Vit essit iligent eliquodi omnimpe riatenem quid quos mi, sum inveliquas enda velestrum, voluptaeped quo etur, aturita ditatus, sinventur re magnihicatet et volupta tibus, sit praeces et facipsum restrum sunte</p>
    </div>
  </div>

  <div class="panel p2">
    <div class="copy" style="top:68px">
      <p class="body-text">suntemp<br>elendeliqui<br>autem. Mus ese rem re ipis<br>unt. Dolutae stiam, num excearum aut pario ma nimus. Ucid quo bla que laboris cipiducim fugiant, consed millore hendige nimolore secte nonest quae de por alicill itaerum la num quo doluptam veni-hic aeperiam inima voluptur ad magnatis pro custem qui autatur as eost accustistis veni sedi doles corum apientem accus es explaut fugiam, sitiur rem que rest reptat rehenimpore nis et la ium aut asperum dolorro</p>
    </div>
  </div>

  <div class="photo team" role="img" aria-label="Group photo of six smiling nurses in scrubs standing in a hospital corridor"></div>

  <div class="panel p3">
    <div class="copy" style="top:124px">
      <h2 class="heading">HEADING</h2>
      <p class="body-text">vitaes ditas nusam eum sitas andestibus magnimped-it a comnis alit ilitatiat andit evellabore et fuga. Ovid maximil laborumque dolut auta nullore henimusdam eost, ulligna tibusa quodit, ni dellent veliquo tem ea vit hictatenti blacess imuscii strumque maio</p>
      <p class="body-text">Ihiliassunt quia quia volestotatem fuga. Berovit ate-moll atusam fugit am voluptas assinctiis modi seque venitatur? Ribus, cullab ium que volut labora dellessit, sequi doluptaquis et dis dolupta se sit, sin ratetur sit od qui di intur rerrore icabo. Nam, consequ iasit, asperume pa dem rehendi gnatet, cum dolo everrum endiciis mi, quia custi cor sit de ma consera tatemo-lupta aut de quia eost fuga. Icime et optio beatet fugit autectur, coraecto dolest voluptat.</p>
      <h2 class="heading" style="margin-top:10px">HEADING</h2>
      <p class="body-text">Dolestionet faccus repreptur mintio to dollent, quiam, sim quas voloreris ea quas serspis asit, sequi con-sendis isci torpor sequia ipid molo est aut minum impor re am quis essin nis dereped mosam hilit aut quo blabori tiorem. Debit veribus et ut quo vidusdam fugit facepudi alit, con cuptatempor molo ea dollicip-sus solorio omnis ut asint mo optas simenimpor ma dolore vel inctorrum qui repersp editati oremque eosto torrumq uisque volorpo rrovidus nem quae parum ne et auditaturest quiam ad que odio. Et et, expland aecti-aesti comnienducid quiam la cus alique solupissit ea as ipsum re porpore ssequi derumet, sam, si voluptis exeruptaque doleser rumqui unt.</p>
    </div>
  </div>
</section>

</body>
</html>
```